Customer Quotes Page

We want to create a fun looking customer quotes page. The point of this project is to be get creative with the treatment of the quotes. Our current version of the page just has them listed in two columns, which is pretty boring. We need something more interesting but it should still fit into our site. Attached is the current Testimonials page as it looks now. The two column layout does not have to be maintained, you can list the manager quotes above the resident quotes. Also not all quotes have to be used, we just need to see 5-10 from the resident and management categories.
The header and footer is already designed, so those elements need to stay the same. The background color also needs to remain same (light fuzzy gray)
Here is a site that we like: https://plumcrestapp.com/about/ (take a look at the "What people are saying" section). But this is just an example, we might like something radically different. The point is to be as creative with the quote boxes as possible. A very refined but subdued approach might also be interesting.
FINAL FILE SHOULD BE A PSD FILE WITH LAYERS. WE WILL CODE THE PAGE OURSELVES.
What we're most interested in this contest is the graphic treatment of the quotes. Right now they're simply gray boxes. We'd like to see what you can do with this. The layout of the page can remain same (two-column) but a 1 column layout is also fine. Also please don't add any additional elements to the page like stock photo. We are only interested in the treatment of the quotes and anything goes whether it is very elegant, cartoony, bold and colorful, hand-drawn, 3D, textured......

```html
<!DOCTYPE html>
<html lang="en">
<head>
<meta charset="utf-8">
<title>TowerNest.com – Testimonials</title>
<link href="https://fonts.googleapis.com/css2?family=Open+Sans:ital,wght@0,400;0,600;0,700;1,400&family=Oswald:wght@500;600&display=swap" rel="stylesheet">
<style>
  :root{
    --page-bg:#ebebeb;
    --top-strip:#2e2e2e;
    --header-bg:#f4f4f4;
    --nav-dark:#3a3a3a;
    --nav-light:#555555;
    --nav-text:#e6e6e6;
    --demo-orange:#e9a21f;
    --brand-red:#d8232a;
    --soft-pink:#f3a9ae;
    --ink:#333333;
    --muted:#8a8a8a;
    --card-bg:#ffffff;
    --footer-bg:#2b2b2b;
    --footer-text:#9b9b9b;
    --footer-head:#d6d6d6;
  }
  *{box-sizing:border-box;margin:0;padding:0}
  html,body{width:1200px;height:900px;overflow:hidden;background:var(--page-bg)}
  body{font-family:"Open Sans",Arial,sans-serif;color:var(--ink);position:relative}

  .top-strip{height:14px;background:var(--top-strip)}
  .site-header{height:66px;background:var(--header-bg);display:flex;align-items:center;justify-content:space-between;padding:0 150px}
  .brand{display:flex;align-items:center;gap:8px;font-weight:700;font-size:26px;color:var(--brand-red);letter-spacing:-.5px}
  .brand-mark{width:14px;height:14px;background:var(--brand-red)}
  .tagline{width:300px;font-size:11px;line-height:1.45;color:var(--muted);border-left:1px solid #ccc;padding-left:14px}

  .main-nav{height:32px;margin:0 150px;background:linear-gradient(var(--nav-light),var(--nav-dark));display:flex}
  .main-nav a{flex:1;display:flex;align-items:center;justify-content:center;text-align:center;font-size:10px;line-height:1.1;color:var(--nav-text);text-decoration:none;border-right:1px solid #2a2a2a}
  .main-nav a.current{background:#2a2a2a}
  .main-nav a.demo{background:var(--demo-orange);color:#3a2a00;font-weight:600}

  .testimonials{position:relative;margin:0 150px;height:628px;background:var(--page-bg)}
  .page-title{position:absolute;left:10px;top:16px;font-family:"Oswald",sans-serif;font-size:20px;color:var(--brand-red);letter-spacing:1px;border-bottom:2px solid var(--soft-pink);padding-right:30px}
  .column-labels{position:absolute;left:0;right:0;top:52px;display:flex;justify-content:center;gap:14px;align-items:center}
  .column-label{font-family:"Oswald",sans-serif;font-size:13px;color:var(--brand-red);letter-spacing:.5px}
  .label-icon{width:26px;height:26px}
  .spine{position:absolute;left:449px;top:92px;bottom:10px;border-left:2px dashed var(--soft-pink)}

  .quote{position:absolute;width:330px}
  .quote-card{position:relative;height:96px;padding:16px 26px 12px 30px;font-size:11px;line-height:1.5;color:var(--ink)}
  .quote-card svg.card-shape{position:absolute;inset:0;width:100%;height:100%;z-index:0}
  .quote-card p{position:relative;z-index:1}
  .pennant{position:absolute;top:-10px;width:22px;height:22px;z-index:2}
  .quote.left .pennant{left:-8px}
  .quote.right .pennant{right:-8px}
  .attribution{display:flex;align-items:center;gap:6px;margin-top:8px;font-size:10.5px}
  .attribution::before{content:"";flex:1;height:2px;background:var(--soft-pink)}
  .attribution strong{color:var(--brand-red);font-weight:700}
  .quote.left .attribution{flex-direction:row}
  .quote.right .attribution{flex-direction:row-reverse}

  .site-footer{position:absolute;left:0;right:0;bottom:0;height:160px;background:var(--footer-bg);padding:24px 150px 0}
  .footer-columns{display:flex;gap:60px}
  .footer-col h4{font-size:11px;font-weight:600;color:var(--footer-head);margin-bottom:8px}
  .footer-col li{list-style:none;font-size:10.5px;color:var(--footer-text);line-height:1.6}
  .footer-phone{font-size:18px;color:var(--footer-head);font-weight:600;margin-bottom:8px}
  .copyright{margin-top:14px;font-size:9.5px;color:#6f6f6f}
</style>
</head>
<body>
  <div class="top-strip"></div>
  <header class="site-header">
    <div class="brand"><span class="brand-mark"></span>TowerNest.com</div>
    <p class="tagline">The Ultimate Integrated Platform for Residential Property Managers &amp; Their Communities</p>
  </header>
  <nav class="main-nav">
    <a href="#">Home</a>
    <a href="#">About<br>TowerNest</a>
    <a href="#">Management<br>Features</a>
    <a href="#">Resident<br>Features</a>
    <a href="#">Professional<br>Services</a>
    <a href="#" class="current">Testimonials</a>
    <a href="#">Support</a>
    <a href="#" class="demo">Request a<br>Demo</a>
  </nav>

  <main class="testimonials">
    <h1 class="page-title">TESTIMONIALS</h1>
    <div class="column-labels">
      <span class="column-label">MANAGER QUOTES</span>
      <svg class="label-icon" viewBox="0 0 26 26"><circle cx="13" cy="13" r="12" fill="none" stroke="#d8232a" stroke-width="2"/><circle cx="13" cy="10" r="4" fill="#d8232a"/><path d="M6 21c1.5-4 4-5 7-5s5.5 1 7 5" fill="#d8232a"/></svg>
      <svg class="label-icon" viewBox="0 0 26 26"><circle cx="13" cy="13" r="12" fill="none" stroke="#d8232a" stroke-width="2"/><path d="M6 14l7-7 7 7v6H6z" fill="#d8232a"/></svg>
      <span class="column-label">RESIDENT QUOTES</span>
    </div>
    <div class="spine"></div>

    <article class="quote left" style="left:90px;top:100px">
      <div class="quote-card">
        <svg class="card-shape" viewBox="0 0 330 96" preserveAspectRatio="none"><polygon points="8,6 330,0 322,90 0,96" fill="#fff" stroke="#d9d9d9"/></svg>
        <svg class="pennant" viewBox="0 0 22 22"><polygon points="2,2 20,8 6,20" fill="#2b2b2b"/></svg>
        <p>Our front desk runs smoother than ever, and residents notice the difference every single day.</p>
      </div>
      <div class="attribution"><strong>— Dana R., Property Manager</strong></div>
    </article>

    <article class="quote right" style="left:480px;top:160px">
      <div class="quote-card">
        <svg class="card-shape" viewBox="0 0 330 96" preserveAspectRatio="none"><polygon points="0,0 322,6 330,96 8,90" fill="#fff" stroke="#d9d9d9"/></svg>
        <svg class="pennant" viewBox="0 0 22 22"><polygon points="20,2 2,8 16,20" fill="#2b2b2b"/></svg>
        <p>I get a text the moment a delivery arrives. No more waiting in the lobby.</p>
      </div>
      <div class="attribution"><strong>— Priya S., Resident</strong></div>
    </article>

    <article class="quote left" style="left:90px;top:270px">
      <div class="quote-card">
        <svg class="card-shape" viewBox="0 0 330 96" preserveAspectRatio="none"><polygon points="0,0 322,8 330,94 6,90" fill="#fff" stroke="#d9d9d9"/></svg>
        <svg class="pennant" viewBox="0 0 22 22"><polygon points="2,2 20,8 6,20" fill="#2b2b2b"/></svg>
        <p>Package tracking alone saved our staff hours each week. Setup was quick and painless.</p>
      </div>
      <div class="attribution"><strong>— Marco L., Resident Manager</strong></div>
    </article>

    <article class="quote right" style="left:480px;top:330px">
      <div class="quote-card">
        <svg class="card-shape" viewBox="0 0 330 96" preserveAspectRatio="none"><polygon points="6,6 330,0 324,92 0,96" fill="#fff" stroke="#d9d9d9"/></svg>
        <svg class="pennant" viewBox="0 0 22 22"><polygon points="20,2 2,8 16,20" fill="#2b2b2b"/></svg>
        <p>Booking the gym and party room takes seconds from my phone.</p>
      </div>
      <div class="attribution"><strong>— Owen K., Resident</strong></div>
    </article>

    <article class="quote left" style="left:90px;top:440px">
      <div class="quote-card">
        <svg class="card-shape" viewBox="0 0 330 96" preserveAspectRatio="none"><polygon points="10,0 330,6 322,96 0,88" fill="#fff" stroke="#d9d9d9"/></svg>
        <svg class="pennant" viewBox="0 0 22 22"><polygon points="2,2 20,8 6,20" fill="#2b2b2b"/></svg>
        <p>Maintenance requests are logged, assigned and closed without a single lost slip of paper.</p>
      </div>
      <div class="attribution"><strong>— Helen T., Building Director</strong></div>
    </article>

    <article class="quote right" style="left:480px;top:500px">
      <div class="quote-card">
        <svg class="card-shape" viewBox="0 0 330 96" preserveAspectRatio="none"><polygon points="0,6 324,0 330,90 8,96" fill="#fff" stroke="#d9d9d9"/></svg>
        <svg class="pennant" viewBox="0 0 22 22"><polygon points="20,2 2,8 16,20" fill="#2b2b2b"/></svg>
        <p>The community board makes our building feel like a real neighborhood.</p>
      </div>
      <div class="attribution"><strong>— Lena M., Resident</strong></div>
    </article>
  </main>

  <footer class="site-footer">
    <div class="footer-columns">
      <div class="footer-col"><h4>Company</h4><ul><li>About Us</li><li>Careers</li><li>Contact</li><li>Privacy</li></ul></div>
      <div class="footer-col"><h4>Features</h4><ul><li>Front Desk</li><li>Packages</li><li>Maintenance</li><li>Amenities</li></ul></div>
      <div class="footer-col"><h4>Partner Network</h4><ul><li>Vendors</li><li>Integrations</li><li>Resellers</li></ul></div>
      <div class="footer-col"><h4>Sales / Support</h4><p class="footer-phone">1(800) 555-0176</p><h4>Stay In Touch</h4><ul><li>Newsletter</li><li>Blog</li></ul></div>
    </div>
    <p class="copyright">© 2024 TowerNest.com. All rights reserved. Terms of Use. Privacy Policy.</p>
  </footer>
</body>
</html>
```